Merrow Consulting needs a business card design

Merrow Consulting is a small business that consults and trains Australia wide in Workplace Health and Safety, Environment and Quality Management Systems.

Clients are typically smaller businesses with 50 to 200 employees but there are some large clients.

Communication is often by email, although mobile is used as well.

Merrow Consulting
41 Tulwin Ferris Road
Carrowdale, QLD 4273
0438 291 064

```html
<!DOCTYPE html>
<html lang="en">
<head>
<meta charset="utf-8">
<title>Merrow Consulting – Business Card</title>
<link href="https://fonts.googleapis.com/css2?family=Open+Sans:wght@600;700&family=Questrial&display=swap" rel="stylesheet">
<style>
  :root {
    --backdrop: #3b3b3d;
    --paper: #ffffff;
    --brand-red: #c8202e;
    --brand-red-light: #e3303a;
    --brand-red-dark: #7f1a20;
    --ink: #2f2f31;
    --rule: #3a3a3a;
  }
  * { margin: 0; padding: 0; box-sizing: border-box; }
  html, body {
    width: 1200px; height: 1000px; overflow: hidden;
    background: var(--backdrop);
  }
  .canvas { position: relative; width: 1200px; height: 1000px; }

  .card {
    position: absolute;
    width: 740px; height: 420px;
    left: 230px;
    box-shadow: 0 4px 10px rgba(0,0,0,.35);
  }

  /* Front of card */
  .card--front { top: 32px; background: var(--paper); }
  .card--front .brand-mark {
    position: absolute; left: 116px; top: 36px;
    width: 124px; height: 124px; border-radius: 50%;
    background: var(--brand-red);
  }
  .card--front .brand-name {
    position: absolute; left: 252px; top: 50px;
    font: 600 32px "Open Sans", sans-serif;
    color: var(--brand-red);
    letter-spacing: 0.5px;
    text-transform: uppercase;
  }
  .card--front .brand-rule {
    position: absolute; left: 252px; top: 102px;
    width: 378px; height: 2px; background: var(--brand-red);
  }
  .card--front .tagline {
    position: absolute; left: 268px; top: 114px;
    font: 600 19px "Open Sans", sans-serif;
    color: var(--brand-red);
    word-spacing: 2px;
  }
  .person-name {
    position: absolute; left: 28px; top: 206px;
    font: 700 28px "Questrial", sans-serif;
    color: var(--ink); letter-spacing: 3px;
    font-variant: small-caps;
  }
  .person-title {
    position: absolute; left: 28px; top: 244px;
    font: 27px "Questrial", sans-serif;
    color: var(--ink); letter-spacing: 2px;
  }
  .divider {
    position: absolute; left: 0; right: 0; top: 291px;
    height: 2px; background: var(--rule);
  }
  .contact {
    position: absolute; left: 28px; top: 304px;
    list-style: none;
    font: 23px/29px "Questrial", sans-serif;
    color: var(--ink); letter-spacing: 1.8px;
  }

  /* Back of card */
  .card--back {
    top: 520px;
    background: linear-gradient(160deg, var(--brand-red-light) 0%, var(--brand-red) 45%, var(--brand-red-dark) 100%);
    color: #fff; text-align: center;
  }
  .card--back .brand-mark {
    position: absolute; left: 290px; top: 36px;
    width: 200px; height: 200px; border-radius: 50%;
    background: #fff;
  }
  .card--back .brand-name {
    position: absolute; left: 0; right: 0; top: 266px;
    font: 600 49px "Open Sans", sans-serif;
    text-transform: uppercase; letter-spacing: 0.5px;
  }
  .card--back .brand-rule {
    position: absolute; left: 102px; width: 556px; top: 338px;
    height: 3px; background: #fff;
  }
  .card--back .tagline {
    position: absolute; left: 0; right: 0; top: 348px;
    font: 600 29px "Open Sans", sans-serif; word-spacing: 3px;
  }
</style>
</head>
<body>
<main class="canvas">
  <section class="card card--front" aria-label="Business card front">
    <div class="brand-mark"></div>
    <div class="brand-name">Merrow Consulting</div>
    <div class="brand-rule"></div>
    <div class="tagline">Health | Environmental | Quality</div>
    <div class="person-name">Liam Harrow</div>
    <div class="person-title">President and CEO</div>
    <div class="divider"></div>
    <ul class="contact">
      <li>41 Tulwin Ferris Road ◆ Carrowdale, QLD 4273</li>
      <li>P: 0438 291 064</li>
      <li>E: liam.harrow@merrowmail.com</li>
    </ul>
  </section>

  <section class="card card--back" aria-label="Business card back">
    <div class="brand-mark"></div>
    <div class="brand-name">Merrow Consulting</div>
    <div class="brand-rule"></div>
    <div class="tagline">Health | Environmental | Quality</div>
  </section>
</main>
</body>
</html>
```